Business Card Design

We are looking for a double sided business card.

On one side would be our logo

On the Other Side

Martin Kolby
Sales and Marketing

Phone/Text Logo and 530-418-2763
Email Logo and info@plumvalepets.com
Website Logo and www.plumvalepets.com
Facebook Logo and plumvale pets
Instagram Logo and plumvale_pets

Target Market(s)

Pet owners

Contact Information for Business Card

In project description

Requirements
Must have
• Logo

```html
<!DOCTYPE html>
<html lang="en">
<head>
<meta charset="utf-8">
<title>Plumvale Pets – Business Card</title>
<link href="https://fonts.googleapis.com/css2?family=Michroma&family=Roboto:wght@400;500;700&display=swap" rel="stylesheet">
<style>
  :root {
    --backdrop: #4a3b2c;
    --card-black: #111111;
    --card-black-soft: #262626;
    --accent: #f6b21b;
    --accent-deep: #e8890c;
    --text-light: #f2f2f2;
    --text-muted: #c9c9c9;
    --silver-light: #f4f4f4;
    --silver-mid: #cfcfcf;
    --silver-dark: #9a9a9a;
    --ink: #2a2a2a;
  }
  * { margin: 0; padding: 0; box-sizing: border-box; }
  html, body { width: 900px; height: 1200px; overflow: hidden; }
  body {
    background: var(--backdrop);
    font-family: "Roboto", Arial, sans-serif;
    position: relative;
  }
  .card {
    position: absolute;
    left: 60px;
    width: 780px;
    height: 450px;
    border-radius: 22px;
    overflow: hidden;
    box-shadow: 0 14px 30px rgba(0,0,0,.45);
  }
  /* Front */
  .card-front {
    top: 110px;
    background: radial-gradient(ellipse at 65% 50%, var(--card-black-soft), var(--card-black) 70%);
  }
  .front-logo {
    position: absolute; left: 46px; top: 56px;
    font-family: "Michroma", sans-serif;
    font-size: 34px; color: var(--text-light);
    letter-spacing: 2px; line-height: 1;
  }
  .name-tag {
    position: absolute; right: 0; top: 44px;
    padding-right: 40px; text-align: right;
    border-right: 12px solid var(--accent);
  }
  .name-tag .person { font-size: 28px; font-weight: 700; color: var(--accent); }
  .name-tag .role { font-size: 17px; color: var(--text-light); margin-top: 4px; }
  .mark-placeholder {
    position: absolute; left: 470px; top: 140px;
    width: 170px; height: 170px; border-radius: 50%;
    background: linear-gradient(160deg, #5a5a5a, #2b2b2b);
  }
  .contact-list {
    position: absolute; left: 46px; bottom: 48px;
    list-style: none;
  }
  .contact-list li {
    display: flex; align-items: center; gap: 12px;
    font-size: 17px; color: var(--text-muted);
    margin-top: 12px;
  }
  .contact-list svg { width: 20px; height: 20px; fill: var(--accent); }
  .social-list {
    position: absolute; left: 560px; top: 328px; list-style: none;
  }
  .social-list li {
    display: flex; align-items: center; gap: 10px;
    font-size: 16px; color: var(--text-light); margin-top: 10px;
  }
  .social-list .dot {
    width: 18px; height: 18px; border-radius: 50%; background: var(--accent);
  }
  .accent-band {
    position: absolute; right: 0; bottom: 0; width: 780px; height: 450px;
  }
  /* Back */
  .card-back {
    top: 640px;
    background: linear-gradient(135deg, var(--silver-light) 0%, var(--silver-mid) 45%, var(--silver-light) 60%, var(--silver-dark) 100%);
    text-align: center;
  }
  .back-mark {
    position: absolute; left: 330px; top: 60px;
    width: 120px; height: 120px; border-radius: 50%;
    background: linear-gradient(160deg, #6a6a6a, #2e2e2e);
  }
  .back-logo {
    position: absolute; left: 0; right: 0; top: 228px;
    font-family: "Michroma", sans-serif;
    font-size: 44px; color: var(--ink); letter-spacing: 3px;
  }
  .back-web {
    position: absolute; left: 0; right: 0; top: 320px;
    font-family: "Michroma", sans-serif;
    font-size: 20px; color: var(--ink); letter-spacing: 3px;
  }
</style>
</head>
<body>
  <section class="card card-front">
    <svg class="accent-band" viewBox="0 0 780 450" aria-hidden="true">
      <polygon points="560,450 600,410 780,410 780,450" fill="var(--accent)"/>
      <polygon points="700,450 740,410 780,410 780,450" fill="var(--accent-deep)"/>
    </svg>

    <div class="front-logo">PLUMVALE PETS</div>

    <div class="name-tag">
      <div class="person">Martin Kolby</div>
      <div class="role">Sales and Marketing</div>
    </div>

    <div class="mark-placeholder"></div>

    <ul class="contact-list">
      <li>
        <svg viewBox="0 0 24 24" aria-hidden="true"><path d="M6.6 10.8a15.1 15.1 0 0 0 6.6 6.6l2.2-2.2c.3-.3.7-.4 1-.2 1.1.4 2.3.6 3.6.6.6 0 1 .4 1 1V20c0 .6-.4 1-1 1C10.6 21 3 13.4 3 4c0-.6.4-1 1-1h3.5c.6 0 1 .4 1 1 0 1.3.2 2.5.6 3.6.1.3 0 .7-.2 1z"/></svg>
        530-418-2763
      </li>
      <li>
        <svg viewBox="0 0 24 24" aria-hidden="true"><path d="M3 5h18v14H3z M3 5l9 7 9-7" fill="none" stroke="var(--accent)" stroke-width="2"/></svg>
        info@plumvalepets.com
      </li>
      <li>
        <svg viewBox="0 0 24 24" aria-hidden="true"><g fill="none" stroke="var(--accent)" stroke-width="2"><circle cx="12" cy="12" r="9"/><path d="M3 12h18M12 3c3 3 3 15 0 18M12 3c-3 3-3 15 0 18"/></g></svg>
        www.plumvalepets.com
      </li>
    </ul>

    <ul class="social-list">
      <li><span class="dot"></span>plumvale pets</li>
      <li><span class="dot"></span>plumvale_pets</li>
    </ul>
  </section>

  <section class="card card-back">
    <div class="back-mark"></div>
    <div class="back-logo">PLUMVALE PETS</div>
    <div class="back-web">WWW.PLUMVALEPETS.COM</div>
  </section>
</body>
</html>
```